professional health club Info Flyer

we need a professional health club DL flyer that will provide information regarding our 24/7 health club services to enquiries whilst we are unstaffed. these will be placed outside on main street.

www.vitrova.club

On the reverse side, we want to offer 2 introductory specials;
1. free 7 day trial
2. Membership, classes & personal training introductory month3 personal training sessions and month 24/7 membership and classes for $99.95 (saving of over $159.85)
conditions: valid for new members only

SIZE: DL with double sided

Target Market(s)

professional, male and female of all ages (in particular those 30+)

Industry/Entity Type

Health And Wellness

Colors
33a6d7
abd037
f78f20
ffffff

Requirements
Must have
• - professional allied health feel about flyer with images
• - contact details
• - services provided include 24/7 memberships, classes, special population group training, Exercise physiology, physiotherapy, massage, nutrition, rehabilitation.
• - a catch to get them to contact us
• - our slogan "We are here to improve your quality of life"

```html
<!DOCTYPE html>
<html lang="en">
<head>
<meta charset="utf-8">
<title>Vitrova Health Club – DL Flyer</title>
<link href="https://fonts.googleapis.com/css2?family=Oswald:wght@600;700&family=Jost:ital,wght@0,400;0,500;0,600;1,500&family=Roboto:ital,wght@0,700;0,900;1,900&display=swap" rel="stylesheet">
<style>
  :root{
    --navy:#1b4289;
    --navy-deep:#143670;
    --sky:#33a6d7;
    --lime:#7bbf3c;
    --orange:#f78f20;
    --gold:#f7b51e;
    --paper:#efefec;
    --white:#ffffff;
    --ink:#1c1c1c;
    --stage:#1e1e1e;
  }
  *{box-sizing:border-box;margin:0;padding:0}
  html,body{width:1176px;height:1200px;overflow:hidden;background:var(--stage)}
  .flyer{position:absolute;top:85px;width:486px;height:1030px;overflow:hidden}
  .flyer--front{left:77px;background:var(--paper)}
  .flyer--back{left:613px;background:var(--white)}
  .flyer svg.art{position:absolute;inset:0;z-index:0}
  .flyer > :not(.art){z-index:1}

  /* front */
  .brand{position:absolute;top:44px;left:60px;display:flex;align-items:center;gap:16px}
  .brand__mark{width:62px;height:62px;border-radius:50%;background:var(--sky)}
  .brand__name{font-family:'Roboto',sans-serif;font-weight:900;font-size:46px;color:var(--navy);letter-spacing:1px;line-height:1}
  .brand__name small{display:block;font-size:17px;letter-spacing:2px;margin-top:6px}
  .tagline{position:absolute;top:138px;left:0;width:486px;text-align:center;font-family:'Roboto',sans-serif;font-style:italic;font-weight:900;font-size:24px;color:var(--navy)}
  .hours{position:absolute;top:735px;right:46px;font-family:'Roboto',sans-serif;font-weight:900;font-size:118px;color:var(--gold);letter-spacing:-2px;line-height:1}
  .services{position:absolute;top:858px;left:220px;width:230px;text-align:center;font-family:'Roboto',sans-serif;font-weight:900;font-size:41px;color:var(--gold);line-height:1}
  .web{position:absolute;top:965px;left:178px;font-family:'Roboto',sans-serif;font-weight:700;font-size:32px;color:var(--white);letter-spacing:1px}
  .badge{position:absolute;top:836px;left:26px;width:152px;height:152px}
  .badge svg{position:absolute;inset:0}
  .badge__text{position:absolute;top:37px;left:0;width:152px;font-family:'Oswald',sans-serif;font-weight:700;font-size:26px;line-height:1;color:var(--white);text-align:center}

  /* back */
  .headline{position:absolute;top:38px;left:30px;font-family:'Oswald',sans-serif;font-weight:700;font-size:44px;line-height:1.18;color:var(--gold)}
  .offer{position:absolute;top:172px;left:30px;width:430px;font-family:'Jost',sans-serif;color:var(--white)}
  .offer__title{font-size:22px;font-weight:500;line-height:1.15;text-transform:uppercase}
  .offer__list{list-style:none;margin-top:20px}
  .offer__item{position:relative;padding-left:26px;font-size:15.5px;line-height:1.3;text-align:justify;margin-bottom:10px}
  .offer__num{position:absolute;left:0;top:1px;width:19px;height:19px;border-radius:50%;background:var(--gold);border:2px solid var(--white);color:var(--ink);font-size:11px;font-weight:600;text-align:center;line-height:15px}
  .offer__item strong{font-weight:600}
  .price{color:var(--gold);font-weight:600}
  .offer__cond{padding-left:26px;font-style:italic;font-weight:500;font-size:13.5px;margin:-2px 0 18px}
  .ticks{list-style:none}
  .tick{position:relative;padding-left:26px;font-size:16px;line-height:1.45;margin-bottom:6px}
  .tick svg{position:absolute;left:0;top:4px}
  .hours--back{position:absolute;top:745px;left:34px;font-family:'Roboto',sans-serif;font-weight:900;font-size:82px;color:var(--orange);letter-spacing:-2px;line-height:1}
  .contact{position:absolute;top:848px;left:30px;font-family:'Jost',sans-serif;font-size:41px;font-weight:400;color:var(--orange);letter-spacing:1px;line-height:1}
  .phone{position:absolute;top:900px;left:30px;font-family:'Roboto',sans-serif;font-weight:900;font-size:48px;color:var(--navy);letter-spacing:1px;line-height:1}
  .address{position:absolute;top:965px;left:30px;font-family:'Jost',sans-serif;font-style:normal;font-size:16.5px;line-height:1.4;color:var(--ink)}
  .mail{position:absolute;top:966px;left:283px;display:flex;align-items:center;gap:10px;font-family:'Jost',sans-serif;font-size:16.5px;line-height:1.3;color:var(--ink)}
</style>
</head>
<body>

<section class="flyer flyer--front">
  <svg class="art" width="486" height="1030" viewBox="0 0 486 1030">
    <defs>
      <linearGradient id="peopleTone" x1="0" y1="0" x2="1" y2="1">
        <stop offset="0" stop-color="#c69877"/><stop offset=".5" stop-color="#3a3a3a"/><stop offset="1" stop-color="#d9d9d9"/>
      </linearGradient>
      <linearGradient id="gymTone" x1="0" y1="0" x2="0" y2="1">
        <stop offset="0" stop-color="#cfd6dc"/><stop offset=".45" stop-color="#6c7680"/><stop offset="1" stop-color="#3a4650"/>
      </linearGradient>
      <linearGradient id="navyFade" x1="0" y1="0" x2="0" y2="1">
        <stop offset="0" stop-color="#1b4289" stop-opacity="0"/><stop offset=".45" stop-color="#1b4289"/><stop offset="1" stop-color="#1b4289"/>
      </linearGradient>
    </defs>
    <rect x="20" y="200" width="340" height="480" rx="30" fill="url(#peopleTone)" opacity=".85" role="img" aria-label="Photo: a man and a woman in gym wear doing dumbbell exercises"/>
    <path d="M0,1030 L0,860 C40,620 250,560 486,330 L486,1030 Z" fill="url(#gymTone)" role="img" aria-label="Photo: interior of the gym with cardio machines and weight benches"/>
    <rect x="0" y="700" width="486" height="330" fill="url(#navyFade)"/>
    <path d="M0,870 C40,620 250,560 486,330 L486,268 C290,520 40,560 0,830 Z" fill="var(--lime)"/>
    <path d="M470,250 C290,460 70,520 34,720" stroke="var(--orange)" stroke-width="3" fill="none"/>
    <path d="M60,1030 C20,960 30,800 80,690" stroke="var(--orange)" stroke-width="16" fill="none"/>
  </svg>

  <div class="brand">
    <span class="brand__mark"></span>
    <div class="brand__name">Vitrova<small>HEALTH CLUB</small></div>
  </div>
  <p class="tagline">Improving your quality of life</p>

  <div class="hours">24/7</div>
  <div class="services">health club services</div>
  <div class="web">www.vitrova.club</div>

  <div class="badge">
    <svg width="152" height="152" viewBox="0 0 152 152">
      <polygon fill="var(--sky)" stroke="var(--white)" stroke-width="2" points="76,2 83,16 93,4 97,19 109,9 110,25 124,18 122,34 137,30 131,45 146,45 137,59 151,62 140,74 151,84 137,90 146,103 131,105 137,120 122,117 124,133 110,127 109,143 97,133 93,148 83,136 76,150 69,136 59,148 55,133 43,143 42,127 28,133 30,117 15,120 21,105 6,103 15,90 1,84 12,74 1,62 15,59 6,45 21,45 15,30 30,34 28,18 42,25 43,9 55,19 59,4 69,16"/>
    </svg>
    <div class="badge__text">FREE<br>7 DAY<br>TRIAL</div>
  </div>
</section>

<section class="flyer flyer--back">
  <svg class="art" width="486" height="1030" viewBox="0 0 486 1030">
    <defs>
      <linearGradient id="athleteTone" x1="0" y1="0" x2="1" y2="1">
        <stop offset="0" stop-color="#e9e9e9"/><stop offset=".45" stop-color="#c99473"/><stop offset="1" stop-color="#2f6fb3"/>
      </linearGradient>
    </defs>
    <path d="M0,0 H486 V690 C400,640 250,530 0,475 Z" fill="var(--navy)"/>
    <path d="M0,475 C250,530 400,640 486,690 L486,700 C380,650 220,560 0,525 Z" fill="var(--lime)"/>
    <path d="M0,530 C220,565 380,655 486,705" stroke="var(--orange)" stroke-width="5" fill="none"/>
    <path d="M290,500 C350,455 450,460 470,540 C492,640 480,760 440,820 C400,850 330,845 280,820 C250,760 250,560 290,500 Z" fill="url(#athleteTone)" opacity=".9" role="img" aria-label="Photo: smiling woman in sportswear doing a seated leg stretch"/>
  </svg>

  <h1 class="headline">We are here to improve<br>your quality of life</h1>

  <div class="offer">
    <p class="offer__title">We offer two introductory<br>specials:</p>
    <ol class="offer__list">
      <li class="offer__item"><span class="offer__num">1</span><strong>FREE 7 DAY TRIAL</strong></li>
      <li class="offer__item"><span class="offer__num">2</span>Membership, classes, personal training introductory month 3 personal training sessions and month 24/7 membership and classes for <span class="price">$99.95 (Saving of over $159.85)</span></li>
    </ol>
    <p class="offer__cond">conditions: valid for new members only</p>
    <ul class="ticks">
      <li class="tick"><svg width="16" height="16" viewBox="0 0 16 16"><circle cx="8" cy="8" r="8" fill="var(--white)"/><path d="M4 8.3l2.6 2.6L12 5.4" stroke="var(--navy)" stroke-width="2.2" fill="none"/></svg>Special population group training,</li>
      <li class="tick"><svg width="16" height="16" viewBox="0 0 16 16"><circle cx="8" cy="8" r="8" fill="var(--white)"/><path d="M4 8.3l2.6 2.6L12 5.4" stroke="var(--navy)" stroke-width="2.2" fill="none"/></svg>Exercise physiology, physiotherapy,<br>massage, nutrition, rehabilitation.</li>
    </ul>
  </div>

  <div class="hours--back">24/7</div>
  <div class="contact">CONTACT US</div>
  <div class="phone">+612 55501234</div>
  <address class="address">27 Harbourview Lane,<br>Kellmont Sydney NSW 2199</address>
  <div class="mail">
    <svg width="34" height="30" viewBox="0 0 34 30"><rect x="1" y="9" width="32" height="20" rx="2" fill="#dfe9f2" stroke="#7a9bb8"/><path d="M1 10l16 11 16-11" stroke="#7a9bb8" fill="none"/><circle cx="17" cy="9" r="8" fill="var(--sky)"/><text x="17" y="13" font-size="11" font-family="Roboto,sans-serif" font-weight="700" fill="#fff" text-anchor="middle">@</text></svg>
    <span>sam@vitrova.club<br>lena@vitrova.club</span>
  </div>
</section>

</body>
</html>
```